BRYLTAllies.co.uk - Mental Health Clinic for Child and Adolescents

Updated 29/01/2018***
I am not sure you guys are getting the idea regards to the opening page / homescreen layout. Can you look at the new images I have uploaded (page 5, 6 and 7) These are some of the layouts I like but to incorporate my chosen images, with the BRYLT commissioner, buttons and a sliding header bar.
I have written a strong brief, I am looking for a website, preferably wordpress as i know they are easy to maintain. I am looking for a one page site, with the top / opening page being full screen image with drop down categories. I have made a rough design, see full brief in word doc attached, there is some freedom to play around with the design aspect but it will need to relay all the content provided. I like a minimal feel. I have also attached some images that may be useful, but will need a new logo for BRYLT Allies. I have attached some logo idea's, it is up to you decide whether you want to use them.
I would prefer the homepage as full screen image, and the categories offered as a drop down or over the main image.
I have also attached linked to some competitors websites:
https://www.verdano-group.co.uk/
http://www.qwmr.org.uk/
Industry/Entity Type
Clinic
Number of Pages Required
1 page
Font styles to use
Look and feel
Each slider illustrates characteristics of the customer's brand and the style your logo design should communicate.

```html
<!DOCTYPE html>
<html lang="en">
<head>
<meta charset="utf-8">
<title>BRYLT Allies – Services and Parents</title>
<link href="https://fonts.googleapis.com/css2?family=Kaushan+Script&family=Lato:wght@300;400&family=Poppins:wght@400;500&display=swap" rel="stylesheet">
<style>
:root{
  --teal:#0f8f7b;
  --mint:#13dcbf;
  --ink:#1a0a17;
  --plum:#5a1a55;
  --paper:#ececec;
  --white:#ffffff;
  --rule:#e2e2e2;
  --text:#2a2a2a;
}
*{box-sizing:border-box;margin:0;padding:0}
html,body{width:1200px;height:1200px;overflow:hidden;background:var(--white)}
body{position:relative;font-family:"Lato",sans-serif;color:var(--text)}
.screen{position:absolute;left:0;width:1200px;overflow:hidden}
.screen--services{top:0;height:591px}
.screen--parents{top:603px;height:597px}
.screen__bg{position:absolute;top:0;bottom:0;right:4px;background:var(--paper)}
.screen--services .screen__bg{left:77px}
.screen--parents .screen__bg{left:71px;right:10px}
.brand{position:absolute;left:0;top:0;width:166px;height:83px;background:var(--white);display:flex;flex-direction:column;align-items:center;justify-content:center;z-index:3}
.screen--parents .brand{width:160px;height:84px}
.brand__name{font-family:"Poppins",sans-serif;font-weight:500;font-size:26px;color:var(--teal);line-height:1;letter-spacing:1px}
.brand__tag{font-family:"Poppins",sans-serif;font-weight:500;font-size:10px;color:var(--plum);margin-top:6px}
.sidebar{position:absolute;left:0;top:83px;width:77px;bottom:0;background:var(--white);z-index:2}
.screen--parents .sidebar{width:71px;top:84px}
.sidebar__item{position:absolute;left:0;width:100%;height:74px;border-bottom:1px solid var(--rule);display:flex;align-items:center;justify-content:center}
.sidebar__item svg{width:30px;height:30px;stroke:#333;fill:none;stroke-width:1.4}
.sidebar__active{position:absolute;left:12px;top:319px;width:156px;height:73px;background:var(--teal);border-right:3px solid #0a3d36;display:flex;align-items:center;gap:26px;padding-left:16px;z-index:4;color:var(--white);font-family:"Poppins",sans-serif;font-size:14px}
.sidebar__active svg{width:28px;height:28px;stroke:var(--white);fill:none;stroke-width:1.4}
.heading{position:absolute;font-family:"Kaushan Script",cursive;font-size:54px;color:var(--ink);line-height:1}
.cycle{position:absolute;left:190px;top:274px;width:48px;height:44px}
.cards{position:absolute;left:255px;top:209px}
.card{position:absolute;top:0;width:156px;height:218px;box-shadow:0 6px 18px rgba(0,0,0,.25);overflow:hidden}
.card svg.card__bg{position:absolute;inset:0}
.card__icon{position:absolute;left:43px;top:28px;width:70px;height:70px;fill:none;stroke-width:2}
.card__label{position:absolute;left:0;right:0;bottom:32px;text-align:center;font-family:"Poppins",sans-serif;font-style:italic;font-size:17px;color:var(--white)}
.photo{position:absolute;top:0;right:0}
.footer{position:absolute;left:0;right:0;text-align:center;font-family:"Poppins",sans-serif;font-size:11px;color:#222}
.intro{position:absolute;left:250px;top:157px;width:556px;font-size:14.4px;line-height:28.8px;font-weight:400}
.intro .lead{margin-top:28.8px}
.intro ul{list-style:none}
.intro li{position:relative;padding-left:27px}
.intro li::before{content:"•";position:absolute;left:0}
</style>
</head>
<body>

<section class="screen screen--services">
  <div class="screen__bg"></div>
  <div class="brand"><span class="brand__name">brylt</span><span class="brand__tag">Where Every Child Counts</span></div>
  <nav class="sidebar">
    <div class="sidebar__item" style="top:0"><svg viewBox="0 0 30 30"><path d="M3 9h24M3 15h24M3 21h24"/></svg></div>
    <div class="sidebar__item" style="top:74px"><svg viewBox="0 0 30 30"><rect x="5" y="4" width="18" height="23"/><path d="M9 10h10M9 14h6M12 23l12-12 2 2-12 12h-2z"/></svg></div>
    <div class="sidebar__item" style="top:148px"><svg viewBox="0 0 30 30"><circle cx="10" cy="11" r="4"/><circle cx="20" cy="11" r="4"/><path d="M3 25c0-6 3-9 7-9s7 3 7 9M13 25c0-6 3-9 7-9s7 3 7 9"/></svg></div>
    <div class="sidebar__item" style="top:222px"></div>
    <div class="sidebar__item" style="top:312px"><svg viewBox="0 0 30 30"><path d="M7 4l5 5-3 3c2 4 5 7 9 9l3-3 5 5-4 3C12 25 5 18 4 8z"/></svg></div>
    <div class="sidebar__item" style="top:395px"><svg viewBox="0 0 30 30"><rect x="3" y="4" width="24" height="22"/><path d="M3 10h24M3 17h24M7 7h10M7 13h14M7 21h6"/></svg></div>
  </nav>
  <div class="sidebar__active"><svg viewBox="0 0 30 30"><path d="M5 25l3-8L22 3l5 5-14 14zM5 5l20 20M8 3l-5 5"/></svg>SERVICES</div>

  <svg class="photo" width="380" height="591" viewBox="820 0 380 591" role="img" aria-label="Photo of a young person sitting at a desk">
    <defs><linearGradient id="dark" x1="0" y1="0" x2="1" y2="1"><stop offset="0" stop-color="#2b221d"/><stop offset=".6" stop-color="#1d1714"/><stop offset="1" stop-color="#120e0c"/></linearGradient></defs>
    <path d="M1200 58 L858 140 Q828 150 836 185 L930 440 Q945 470 985 490 L1200 558 Z" fill="var(--teal)"/>
    <path d="M1200 66 L866 148 Q840 158 846 188 L938 438 Q952 466 990 484 L1200 550 Z" fill="url(#dark)"/>
  </svg>

  <h2 class="heading" style="left:253px;top:110px">Our Services</h2>
  <svg class="cycle" viewBox="0 0 48 44" fill="none" stroke-width="2" stroke-linecap="round">
    <path d="M26 4l-5 5 5 5M21 9h12a10 10 0 0 1 0 20h-2" stroke="var(--mint)"/>
    <path d="M22 40l5-5-5-5M27 35H14a10 10 0 0 1 0-20h2" stroke="var(--ink)"/>
  </svg>

  <div class="cards">
    <div class="card" style="left:0">
      <svg class="card__bg" width="156" height="218"><rect width="156" height="218" fill="var(--ink)"/><path d="M0 0H156V119L0 140Z" fill="var(--mint)"/></svg>
      <svg class="card__icon" viewBox="0 0 70 70" stroke="var(--ink)"><path d="M35 8L6 20l29 12 29-12zM20 26v12c5 5 25 5 30 0V26M62 21v14"/><circle cx="62" cy="38" r="2"/><path d="M10 66c3-12 12-16 25-16s22 4 25 16"/></svg>
      <div class="card__label">ADHD</div>
    </div>
    <div class="card" style="left:181px">
      <svg class="card__bg" width="156" height="218"><rect width="156" height="218" fill="var(--mint)"/><path d="M0 0H156V119L0 140Z" fill="var(--ink)"/></svg>
      <svg class="card__icon" viewBox="0 0 70 70" stroke="var(--white)"><path d="M2 8h66M5 8v44h60V8M35 2v6M35 52l-8 10M35 52l8 10"/><text x="12" y="38" fill="var(--white)" stroke="none" font-family="Poppins,sans-serif" font-size="18">A</text><text x="28" y="44" fill="var(--mint)" stroke="none" font-family="Poppins,sans-serif" font-size="18">B</text><text x="46" y="38" fill="var(--mint)" stroke="none" font-family="Poppins,sans-serif" font-size="18">C</text></svg>
      <div class="card__label">ASD</div>
    </div>
    <div class="card" style="left:365px">
      <svg class="card__bg" width="156" height="218"><rect width="156" height="218" fill="var(--mint)"/><path d="M0 0H156V119L0 140Z" fill="var(--ink)"/></svg>
      <svg class="card__icon" viewBox="0 0 70 70" stroke="var(--white)"><path d="M8 6h54v60H14a6 6 0 0 1-6-6zM14 60h48M14 12h48v44H14z"/><path d="M26 28h20v14H26zM30 35h12"/><path d="M18 6v14l4-4 4 4V6" stroke="var(--mint)"/></svg>
      <div class="card__label">CBT</div>
    </div>
    <div class="card" style="left:546px">
      <svg class="card__bg" width="156" height="218"><rect width="156" height="218" fill="var(--mint)"/><path d="M0 0H156V119L0 140Z" fill="var(--ink)"/></svg>
      <svg class="card__icon" viewBox="0 0 70 70" stroke="var(--white)"><path d="M35 10a15 15 0 0 0-9 27v12h18V37a15 15 0 0 0-9-27zM26 49l9 14 9-14M28 54h14"/><path d="M30 22c0 6 5 8 5 14M40 22c0 6-5 8-5 14M35 0v5M10 23h6M54 23h6M16 6l4 4M54 6l-4 4M8 44h12M50 44h12" stroke="var(--mint)"/></svg>
      <div class="card__label">EMDR</div>
    </div>
  </div>

  <p class="footer" style="top:559px">© 2018 All Rights Reserved.brylt.com</p>
</section>

<section class="screen screen--parents">
  <div class="screen__bg"></div>
  <div class="brand"><span class="brand__name">brylt</span><span class="brand__tag">Where Every Child Counts</span></div>
  <nav class="sidebar">
    <div class="sidebar__item" style="top:0"><svg viewBox="0 0 30 30"><path d="M3 9h24M3 15h24M3 21h24"/></svg></div>
    <div class="sidebar__item" style="top:74px"><svg viewBox="0 0 30 30"><rect x="5" y="4" width="18" height="23"/><path d="M9 10h10M9 14h6M12 23l12-12 2 2-12 12h-2z"/></svg></div>
    <div class="sidebar__item" style="top:148px"><svg viewBox="0 0 30 30"><circle cx="10" cy="11" r="4"/><circle cx="20" cy="11" r="4"/><path d="M3 25c0-6 3-9 7-9s7 3 7 9M13 25c0-6 3-9 7-9s7 3 7 9"/></svg></div>
    <div class="sidebar__item" style="top:222px"><svg viewBox="0 0 30 30"><path d="M5 25l3-8L22 3l5 5-14 14zM5 5l20 20M8 3l-5 5"/></svg></div>
    <div class="sidebar__item" style="top:296px;height:88px"><svg viewBox="0 0 30 30"><path d="M7 4l5 5-3 3c2 4 5 7 9 9l3-3 5 5-4 3C12 25 5 18 4 8z"/></svg></div>
    <div class="sidebar__item" style="top:384px;height:78px"><svg viewBox="0 0 30 30"><rect x="3" y="4" width="24" height="22"/><path d="M3 10h24M3 17h24M7 7h10M7 13h14M7 21h6"/></svg></div>
  </nav>

  <svg class="photo" width="380" height="597" viewBox="810 0 380 597" role="img" aria-label="Photo of a smiling woman with glasses talking with her hands">
    <defs><linearGradient id="warm" x1="0" y1="0" x2="1" y2="1"><stop offset="0" stop-color="#f4efe9"/><stop offset=".45" stop-color="#e7d2c3"/><stop offset=".7" stop-color="#c98b73"/><stop offset="1" stop-color="#efe7e0"/></linearGradient></defs>
    <path d="M1190 57 L850 126 Q822 134 830 165 L926 457 Q940 486 975 498 L1190 557 Z" fill="var(--teal)"/>
    <path d="M1190 65 L858 134 Q836 142 840 168 L934 455 Q948 480 980 490 L1190 549 Z" fill="url(#warm)"/>
  </svg>

  <h2 class="heading" style="left:251px;top:80px">Parents</h2>
  <div class="intro">
    <p>Are you looking for a thorough, efficient, highly accurate screening or assessment for<br>your child?&nbsp; We use both electronic and paper based screening tools so that we can be<br>flexible to what works better around you. We will deliver you the results within 24 hours<br>after our screening tools have been completed, and will make recommendations based<br>around these results.</p>
    <p>Should you opt to have a full ADHD / ASD assessment we aim to have appointments avail-<br>able with 14 days.&nbsp; All of our clinicians have been specifically chosen as they are some of<br>the best in their specialist field.</p>
    <p class="lead">We offer the following assessments:</p>
    <ul>
      <li>ADOS</li>
      <li>ADI-R</li>
      <li>(few more to add at a later date)</li>
    </ul>
  </div>

  <p class="footer" style="top:560px">© 2018 All Rights Reserved.brylt.com</p>
</section>

</body>
</html>
```